Website

I have a client that we built a website for about 10 years ago - https://www.pinloopcards.com.au/

We would like a fresh new design for it that looks more modern. All the elements, info that's on there needs to be the same but the whole design/layout needs to be modernised.

```html
<!DOCTYPE html>
<html lang="en">
<head>
<meta charset="utf-8">
<title>Pinloop Cards – Premium Name Tags &amp; Corporate Badges</title>
<link href="https://fonts.googleapis.com/css2?family=Montserrat:wght@500;600;700;800&family=Poppins:wght@400;500;600&display=swap" rel="stylesheet">
<style>
:root{
  --red:#d5121e;
  --red-dark:#a80c16;
  --ink:#1c1c1c;
  --text:#555;
  --muted:#8a8a8a;
  --line:#e6e6e6;
  --soft:#f4f4f5;
  --pink:#fde7e9;
  --dark:#1d1d1f;
  --white:#fff;
}
*{box-sizing:border-box;margin:0;padding:0}
html,body{width:1200px;height:3872px;overflow:hidden}
body{font-family:"Poppins",sans-serif;color:var(--text);background:var(--white);font-size:14px;line-height:1.6}
h1,h2,h3,h4{font-family:"Montserrat",sans-serif;color:var(--ink)}
a{color:inherit;text-decoration:none}
.wrap{width:1080px;margin:0 auto;position:relative}
.btn{display:inline-block;font-family:"Montserrat",sans-serif;font-weight:600;font-size:13px;padding:11px 22px;border-radius:4px}
.btn-red{background:var(--red);color:var(--white)}
.btn-white{background:var(--white);color:var(--red)}
.btn-outline{border:1.5px solid var(--white);color:var(--white)}

/* top bar */
.topbar{height:40px;background:var(--dark);color:#ccc;font-size:12px}
.topbar .wrap{display:flex;justify-content:space-between;align-items:center;height:40px}
.topbar span{display:inline-flex;align-items:center;gap:6px;margin-right:22px}
.topbar .right span{margin:0 0 0 20px}
.ico{width:13px;height:13px;fill:var(--red)}

/* nav */
.nav{height:72px;border-bottom:1px solid var(--line)}
.nav .wrap{display:flex;justify-content:space-between;align-items:center;height:72px}
.brand{display:flex;align-items:center;gap:10px;font-family:"Montserrat",sans-serif;font-weight:800;font-size:20px;color:var(--red)}
.brand i{width:18px;height:18px;background:var(--red);border-radius:50%;display:block}
.menu{display:flex;gap:30px;font-size:13px;color:var(--ink)}
.menu a.active{color:var(--white);background:var(--red);padding:6px 14px;border-radius:3px;margin:-6px -14px}

/* hero */
.hero{height:448px;background:linear-gradient(120deg,var(--red) 0%,#c40f1a 60%,var(--red-dark) 100%);color:var(--white)}
.hero .wrap{display:flex;align-items:center;height:448px}
.hero-copy{width:520px}
.pill{display:inline-block;background:var(--white);color:var(--red);font-weight:600;font-size:13px;padding:6px 18px;border-radius:20px;margin-bottom:22px}
.hero h1{color:var(--white);font-size:46px;line-height:1.12;font-weight:800;text-transform:uppercase;margin-bottom:18px}
.hero p{font-size:15px;color:#fbe3e4;margin-bottom:28px}
.hero .btn{margin-right:12px}
.hero-art{width:520px;height:380px;margin-left:auto;border-radius:12px;background:radial-gradient(circle at 55% 45%,#f7f7f7 0%,#e8e8e8 40%,rgba(255,255,255,.15) 72%,rgba(255,255,255,0) 100%)}

/* features */
.features{height:170px;display:flex;align-items:center}
.features .wrap{display:flex;justify-content:space-between}
.feat{display:flex;align-items:center;gap:14px;width:250px}
.feat svg{width:44px;height:44px;flex:none}
.feat b{display:block;font-family:"Montserrat",sans-serif;font-size:14px;color:var(--ink);text-transform:uppercase;line-height:1.3}
.feat small{font-size:12px;color:var(--muted)}

/* products */
.products{height:440px;text-align:center;padding-top:24px}
.sec-title{font-size:34px;font-weight:700;margin-bottom:8px}
.sec-sub{font-size:14px;color:var(--muted)}
.prod-row{display:flex;justify-content:space-between;margin-top:40px;padding:0 40px}
.prod{width:160px}
.prod-img{width:130px;height:130px;border-radius:50%;margin:0 auto 14px;background:linear-gradient(135deg,#f3f3f3,#dcdcdc);border:1px solid var(--line)}
.prod h4{font-size:14px;font-weight:600;text-transform:uppercase;line-height:1.35}
.prod a{color:var(--red);font-size:13px;display:inline-block;margin-top:6px;border-bottom:1px solid var(--red)}

/* about */
.about{height:520px}
.about .wrap{display:flex;align-items:center;height:440px}
.about-copy{width:520px}
.about h2{font-size:36px;font-weight:700;margin-bottom:6px}
.about h3{font-size:16px;font-weight:600;margin-bottom:16px}
.about p{font-size:13.5px;margin-bottom:14px}
.about-art{margin-left:auto;width:500px;height:400px;border-radius:14px;background:var(--pink);position:relative;overflow:hidden}
.about-art .person{position:absolute;left:110px;bottom:0;width:300px;height:370px;border-radius:150px 150px 0 0;background:linear-gradient(180deg,#d9cfc8,#4b4b4f)}
.about-art .seal{position:absolute;left:40px;top:60px;width:110px;height:110px;border-radius:50%;background:var(--ink)}

/* why */
.why{height:440px;background:var(--soft);text-align:center;padding-top:60px}
.why-row{display:flex;justify-content:space-between;margin-top:40px}
.why-card{width:248px;height:160px;background:var(--white);border-radius:8px;box-shadow:0 6px 20px rgba(0,0,0,.06);display:flex;flex-direction:column;align-items:center;justify-content:center;gap:12px}
.why-card svg{width:44px;height:44px}
.why-card b{font-family:"Montserrat",sans-serif;font-size:14px;color:var(--ink);text-transform:uppercase;line-height:1.35}

/* testimonials */
.reviews{height:460px;text-align:center;padding-top:50px}
.rev-row{display:flex;gap:30px;justify-content:center;margin-top:40px;position:relative}
.rev{width:470px;text-align:left;background:var(--white);border-radius:8px;box-shadow:0 8px 24px rgba(0,0,0,.08);padding:36px 32px 26px;position:relative}
.rev .quote{position:absolute;right:24px;top:-22px;width:46px;height:46px;border-radius:50%;background:var(--ink);color:var(--white);font:800 34px/54px "Montserrat",sans-serif;text-align:center}
.rev p{font-size:13px;margin-bottom:20px}
.rev b{font-family:"Montserrat",sans-serif;color:var(--ink);font-size:14px}
.rev small{display:block;font-size:12px;color:var(--muted)}
.rev .mark{position:absolute;right:32px;bottom:32px;width:20px;height:20px;border-radius:50%;background:var(--muted)}
.arrow{position:absolute;top:110px;width:30px;height:30px;border-radius:50%;background:var(--white);box-shadow:0 2px 8px rgba(0,0,0,.15);display:flex;align-items:center;justify-content:center}
.arrow.l{left:0}.arrow.r{right:0}
.dots{display:flex;gap:8px;justify-content:center;margin-top:30px}
.dots i{width:7px;height:7px;border-radius:50%;background:#ccc;display:block}
.dots i.on{background:var(--red);box-shadow:0 0 0 3px #f6c6c9}

/* logos */
.clients{height:260px;border-top:1px solid var(--line);border-bottom:1px solid var(--line)}
.clients .wrap{display:flex;justify-content:space-between;align-items:center;height:200px;padding:0 30px}
.client{width:90px;height:46px;background:#d7d7d7;border-radius:6px}
.clients .dots{margin-top:-40px}

/* contact */
.contact{height:560px}
.contact .wrap{display:flex;align-items:center;height:560px}
.contact-info{width:480px}
.contact h2{font-size:34px;font-weight:800;text-transform:uppercase;margin-bottom:10px}
.contact-info > p{font-size:13.5px;margin-bottom:30px}
.socials{display:flex;gap:10px;margin-bottom:40px}
.socials i{width:30px;height:30px;border-radius:50%;background:var(--ink);display:block}
.info-line{display:flex;gap:14px;align-items:flex-start;font-size:13.5px;color:var(--ink);margin-bottom:20px}
.info-line svg{width:16px;height:16px;fill:var(--red);flex:none;margin-top:3px}
.form{margin-left:auto;width:500px;height:470px;background:linear-gradient(160deg,var(--red),var(--red-dark));border-radius:12px;padding:36px 34px}
.form .row{display:flex;gap:14px;margin-bottom:14px}
.field{flex:1;height:42px;background:var(--white);border-radius:4px;padding:0 14px;font-size:12.5px;line-height:42px;color:var(--muted)}
.field.area{height:150px;line-height:1.6;padding-top:12px;margin-bottom:22px}
.form .btn{display:block;text-align:center;background:var(--white);color:var(--red)}

/* footer */
.footer{height:432px;background:var(--dark);color:#bdbdbd;font-size:13px}
.footer .cols{display:flex;height:370px;padding-top:50px}
.col{width:220px}
.col.about-col{width:320px}
.col.news{margin-left:auto;width:300px}
.footer h4{color:var(--white);font-size:16px;margin-bottom:18px}
.footer .brand{color:var(--white);margin-bottom:16px}
.footer .brand i{background:var(--white)}
.footer ul{list-style:none}
.footer li{margin-bottom:6px}
.footer .info-line{color:#bdbdbd;font-size:13px}
.sub-input{height:40px;background:#2c2c2f;border-radius:4px;padding:0 14px;line-height:40px;color:#888;margin:16px 0 12px}
.footer .btn{background:var(--red);color:var(--white);width:100%;text-align:center}
.copy{border-top:1px solid #333;height:62px}
.copy .wrap{display:flex;justify-content:space-between;align-items:center;height:62px;font-size:12px}
</style>
</head>
<body>

<div class="topbar">
  <div class="wrap">
    <div>
      <span><svg class="ico" viewBox="0 0 24 24"><path d="M6.6 10.8a15 15 0 0 0 6.6 6.6l2.2-2.2c.3-.3.7-.4 1-.2 1.1.4 2.3.6 3.6.6.6 0 1 .4 1 1V20c0 .6-.4 1-1 1A17 17 0 0 1 3 4c0-.6.4-1 1-1h3.5c.6 0 1 .4 1 1 0 1.3.2 2.5.6 3.6.1.3 0 .7-.2 1z"/></svg>1300 555 014</span>
      <span><svg class="ico" viewBox="0 0 24 24"><path d="M2 5h20v14H2zm2 2v.5l8 5 8-5V7z"/></svg>info@pinloopcards.com</span>
    </div>
    <div class="right"><span>Register</span><span>Login</span><span>Cart</span></div>
  </div>
</div>

<header class="nav">
  <div class="wrap">
    <div class="brand"><i></i>Pinloop Cards</div>
    <nav class="menu">
      <a class="active">Home</a><a>Products</a><a>Price List</a><a>Re-orders/ Trade info</a><a>Info</a><a>Artwork Requirements</a><a>Payment</a><a>Contact Us</a>
    </nav>
  </div>
</header>

<section class="hero">
  <div class="wrap">
    <div class="hero-copy">
      <span class="pill">Australia's Trusted Badge Manufacturer</span>
      <h1>Premium Name Tags &amp; Corporate Badges</h1>
      <p>Elevate your professional image with our precision-crafted identification solutions. Serving Australian businesses for over 25 years with quality that speaks volumes.</p>
      <a class="btn btn-white">Request a Quote</a><a class="btn btn-outline">View Our Products</a>
    </div>
    <div class="hero-art" role="img" aria-label="Photo of lanyard ID card, name badges and round button badges"></div>
  </div>
</section>

<section class="features">
  <div class="wrap">
    <div class="feat"><svg viewBox="0 0 44 44"><circle cx="22" cy="22" r="20" fill="none" stroke="#d5121e" stroke-width="2"/><path d="M14 22l6 6 10-12" fill="none" stroke="#d5121e" stroke-width="2.5"/></svg><div><b>No Minimum<br>Order*</b><small>on name badges</small></div></div>
    <div class="feat"><svg viewBox="0 0 44 44"><rect x="4" y="14" width="22" height="16" fill="none" stroke="#d5121e" stroke-width="2"/><path d="M26 19h8l6 6v5H26z" fill="none" stroke="#d5121e" stroke-width="2"/><circle cx="12" cy="32" r="3" fill="#d5121e"/><circle cx="33" cy="32" r="3" fill="#d5121e"/></svg><div><b>Fast<br>Delivery</b><small>on name badges</small></div></div>
    <div class="feat"><svg viewBox="0 0 44 44"><circle cx="22" cy="22" r="8" fill="none" stroke="#d5121e" stroke-width="2"/><circle cx="22" cy="22" r="17" fill="none" stroke="#d5121e" stroke-width="2" stroke-dasharray="6 4"/></svg><div><b>Free<br>Setup</b><small>on name badges</small></div></div>
    <div class="feat"><svg viewBox="0 0 44 44"><rect x="8" y="6" width="28" height="32" rx="2" fill="none" stroke="#d5121e" stroke-width="2"/><path d="M14 16h16M14 22h16M14 28h10" stroke="#d5121e" stroke-width="2"/></svg><div><b>Free<br>Postage*</b><small>for badge orders over $400</small></div></div>
  </div>
</section>

<section class="products">
  <div class="wrap">
    <h2 class="sec-title">Our Premium Products</h2>
    <p class="sec-sub">From executive name badges to durable staff tags, we offer identification solutions for every business need.</p>
    <div class="prod-row">
      <div class="prod"><div class="prod-img" role="img" aria-label="Engraved name badge"></div><h4>Engraved<br>Name Badges</h4><a>Read More</a></div>
      <div class="prod"><div class="prod-img" role="img" aria-label="Photo ID card"></div><h4>Photo ID<br>Cards</h4><a>Read More</a></div>
      <div class="prod"><div class="prod-img" role="img" aria-label="Full colour name badge"></div><h4>Full Colour<br>Name Badges</h4><a>Read More</a></div>
      <div class="prod"><div class="prod-img" role="img" aria-label="Round button badge"></div><h4>Button<br>Badges</h4><a>Read More</a></div>
      <div class="prod"><div class="prod-img" role="img" aria-label="Lapel pin"></div><h4>Lapel<br>Pins</h4><a>Read More</a></div>
    </div>
  </div>
</section>

<section class="about">
  <div class="wrap">
    <div class="about-copy">
      <h2>About Us</h2>
      <h3>The best custom name badges for companies Australia.</h3>
      <p>Do you need Name Badges for your company or an upcoming event? At Pinloop Cards, we specialise in producing a range of identity name tags and ID products. Tailor your name tags to suit your exact requirements with a choice of sizes, colours, fittings and finishes.</p>
      <p>Offering a full range of custom name badges, ordering is easy with our user friendly "Build a Badge" step by step process, which is simple to use and ensures you will receive the exact badge required. It only takes a couple of minutes and provides an instant online quote.</p>
      <a class="btn btn-red" style="margin-top:10px">Request a Quote</a>
    </div>
    <div class="about-art">
      <div class="seal" role="img" aria-label="Round quality seal"></div>
      <div class="person" role="img" aria-label="Photo of a smiling businesswoman in a suit"></div>
    </div>
  </div>
</section>

<section class="why">
  <div class="wrap">
    <h2 class="sec-title">Why Choose Us?</h2>
    <p class="sec-sub">When it comes to name badges, tags, and other ID products, trusted in Australia than Pinloop Cards.</p>
    <div class="why-row">
      <div class="why-card"><svg viewBox="0 0 44 44"><circle cx="22" cy="22" r="18" fill="none" stroke="#d5121e" stroke-width="2"/><path d="M14 22l6 6 10-12" fill="none" stroke="#d5121e" stroke-width="2.5"/></svg><b>No Minimum Order<br>on Name Badges</b></div>
      <div class="why-card"><svg viewBox="0 0 44 44"><rect x="4" y="14" width="22" height="16" fill="none" stroke="#d5121e" stroke-width="2"/><path d="M26 19h8l6 6v5H26z" fill="none" stroke="#d5121e" stroke-width="2"/><circle cx="12" cy="32" r="3" fill="#d5121e"/><circle cx="33" cy="32" r="3" fill="#d5121e"/></svg><b>Fast Delivery<br>in Australia</b></div>
      <div class="why-card"><svg viewBox="0 0 44 44"><circle cx="22" cy="22" r="8" fill="none" stroke="#d5121e" stroke-width="2"/><circle cx="22" cy="22" r="17" fill="none" stroke="#d5121e" stroke-width="2" stroke-dasharray="6 4"/></svg><b>Free Setup For<br>Anywhere</b></div>
      <div class="why-card"><svg viewBox="0 0 44 44"><rect x="8" y="6" width="28" height="32" rx="2" fill="none" stroke="#d5121e" stroke-width="2"/><path d="M14 16h16M14 22h16M14 28h10" stroke="#d5121e" stroke-width="2"/></svg><b>Free Postage Badge<br>Orders Over $400</b></div>
    </div>
  </div>
</section>

<section class="reviews">
  <div class="wrap">
    <h2 class="sec-title">What To Say Our Customer</h2>
    <div class="rev-row">
      <span class="arrow l"><svg width="12" height="12" viewBox="0 0 12 12"><path d="M8 2L4 6l4 4" fill="none" stroke="#333" stroke-width="2"/></svg></span>
      <div class="rev"><span class="quote">”</span><p>Our team badges arrived quickly and looked sharp. Ordering online was simple, the proof was clear and the finish on every tag was excellent. We will be ordering again for our next event and recommend them to colleagues.</p><b>Talia Moreno</b><small>Reviewed on 7 Aug, 2025</small><i class="mark"></i></div>
      <div class="rev"><span class="quote">”</span><p>Great service from start to finish. The staff helped us choose the right fittings and colours, and the badges matched our brand perfectly. Delivery was fast and the quality has held up well with daily use by our staff.</p><b>Talia Moreno</b><small>Reviewed on 7 Aug, 2025</small><i class="mark"></i></div>
      <span class="arrow r"><svg width="12" height="12" viewBox="0 0 12 12"><path d="M4 2l4 4-4 4" fill="none" stroke="#333" stroke-width="2"/></svg></span>
    </div>
    <div class="dots"><i></i><i></i><i></i><i class="on"></i><i></i><i></i></div>
  </div>
</section>

<section class="clients">
  <div class="wrap">
    <i class="client"></i><i class="client"></i><i class="client"></i><i class="client"></i><i class="client"></i><i class="client"></i><i class="client"></i>
  </div>
  <div class="dots"><i class="on"></i><i></i><i></i><i></i></div>
</section>

<section class="contact">
  <div class="wrap">
    <div class="contact-info">
      <h2>Get In Touch</h2>
      <p>Have questions or ready to start your order? Our team is here to help. Do you need Name Badges?</p>
      <div class="socials"><i></i><i></i><i></i><i></i></div>
      <div class="info-line"><svg viewBox="0 0 24 24"><path d="M12 2a7 7 0 0 0-7 7c0 5 7 13 7 13s7-8 7-13a7 7 0 0 0-7-7zm0 9.5A2.5 2.5 0 1 1 12 6.5a2.5 2.5 0 0 1 0 5z"/></svg><span>123, Lorem ipsum dolor sit amet,<br>consectetur - 32100</span></div>
      <div class="info-line"><svg viewBox="0 0 24 24"><path d="M6.6 10.8a15 15 0 0 0 6.6 6.6l2.2-2.2c.3-.3.7-.4 1-.2 1.1.4 2.3.6 3.6.6.6 0 1 .4 1 1V20c0 .6-.4 1-1 1A17 17 0 0 1 3 4c0-.6.4-1 1-1h3.5c.6 0 1 .4 1 1 0 1.3.2 2.5.6 3.6.1.3 0 .7-.2 1z"/></svg><span>Phone: 1300 555 014</span></div>
      <div class="info-line"><svg viewBox="0 0 24 24"><path d="M2 5h20v14H2zm2 2v.5l8 5 8-5V7z"/></svg><span>info@pinloopcards.com</span></div>
    </div>
    <div class="form">
      <div class="row"><div class="field">Name</div><div class="field">Email</div></div>
      <div class="row"><div class="field">Phone</div><div class="field">Subject</div></div>
      <div class="field area">How can we help solve your requirements?</div>
      <a class="btn">Submit Now</a>
    </div>
  </div>
</section>

<footer class="footer">
  <div class="wrap cols">
    <div class="col about-col">
      <div class="brand"><i></i>Pinloop Cards</div>
      <p>Australia's trusted manufacturer of premium name badges, signage, and identification solutions since 1998.</p>
    </div>
    <div class="col">
      <h4>Quick Links</h4>
      <ul><li>Home</li><li>Products</li><li>Price List</li><li>Re-orders/ Trade info</li><li>Info</li><li>Artwork Requirements</li><li>Payment Contact Us</li></ul>
    </div>
    <div class="col" style="width:260px">
      <h4>Contact Us</h4>
      <div class="info-line"><svg viewBox="0 0 24 24"><path d="M12 2a7 7 0 0 0-7 7c0 5 7 13 7 13s7-8 7-13a7 7 0 0 0-7-7zm0 9.5A2.5 2.5 0 1 1 12 6.5a2.5 2.5 0 0 1 0 5z"/></svg><span>123, Lorem ipsum dolor sit amet, consectetur - 32100</span></div>
      <div class="info-line"><svg viewBox="0 0 24 24"><path d="M6.6 10.8a15 15 0 0 0 6.6 6.6l2.2-2.2c.3-.3.7-.4 1-.2 1.1.4 2.3.6 3.6.6.6 0 1 .4 1 1V20c0 .6-.4 1-1 1A17 17 0 0 1 3 4c0-.6.4-1 1-1h3.5c.6 0 1 .4 1 1 0 1.3.2 2.5.6 3.6.1.3 0 .7-.2 1z"/></svg><span>Phone: 1300 555 014</span></div>
      <div class="info-line"><svg viewBox="0 0 24 24"><path d="M2 5h20v14H2zm2 2v.5l8 5 8-5V7z"/></svg><span>info@pinloopcards.com</span></div>
    </div>
    <div class="col news">
      <h4>Subscribe to Newsletter</h4>
      <p>Be sure not miss the updates, get deals, and insider news!</p>
      <div class="sub-input">Enter your email</div>
      <a class="btn">Subscribe Now</a>
    </div>
  </div>
  <div class="copy">
    <div class="wrap"><span>© Copyright 2025 Pinloop Cards. All rights reserved.</span><span>Privacy Policy &nbsp;|&nbsp; Terms &amp; Conditions</span></div>
  </div>
</footer>

</body>
</html>
```